Clara Joy Halden- Lantern Waltz- Autumn/Winter Tour Dates

I need high res A3 Tour poster for print and for social media JPG sharing of tour dates.
Also needed Facebook/Twitter Banner Cover Photos of these dates.
Text Needed Below
Clara Joy Halden
Lantern Waltz
Autumn/Winter Tour Dates
03/09 Ravensby Folk Festival
21/09 Swindon- Calder Theatre
01/10 Hitchin- Brackwell Folk Club
17/10 Bath- The Anvil
20/10 Sheffield- Upper Dale Croquet Club
24/10 Birmingham- Orchard Lamp Cafe
26/10 Glasgow- The Nook and Jar
27/10 Edinburgh - The Marble Parlour
08/11 Capital Reel and Ballad Festival- The Crooked Heron
25/11 Lewes- Tandem Record Shop- Live In Store
02/12 Cambridge- The Quayside
27/01 Lincolnshire- Fenmarsh Theatre
Tickets/Info: www.clarajoyhalden-music.example/gigs
(Quotes/Reviews To Put On)
"Outstanding, rich and expressive."            "Vibrant and Experimental"
**** BdM                                                               **** Tunepaths
"Impressive and Invigorating"                        "Enchanting" Acoustic Wire UK
tBarks

Updates
I cannot read the tour dates on most of the submissions so far. They need to be visible to viewers.
Thank You.
Please also be as creative and inventive as possible- not bland.

Target Market(s)
Music Fans- Folk Acoustic Americana
Industry/Entity Type
Media
Font styles to use
Requirements
Must have
- My photo featured prominently
- Look classy and not tacky or OTT
- Look elegant, wintery and eye catching
- The dates must be very clear to read
- Links to Website:

Nice to have
- Something innovative and not boring in terms of layout design
- Perhaps fading/ misty or wintery

Should not have
- Any colours that do not match

```html
<!DOCTYPE html>
<html lang="en">
<head>
<meta charset="utf-8">
<title>Clara Joy Halden – Lantern Waltz – Tour Banner</title>
<link rel="stylesheet" href="https://fonts.googleapis.com/css2?family=Pinyon+Script&family=Libre+Caslon+Text:ital,wght@0,400;0,700;1,700&display=swap">
<style>
:root{
  --page:#dcdcdc;
  --ice-light:#eef5fb;
  --ice-mid:#c9def0;
  --ice-deep:#9cc1e0;
  --navy:#1c4a78;
  --panel:#8eb0da;
  --panel-light:#a6c2e4;
  --header:#eef1f5;
  --white:#ffffff;
  --photo-a:#d7e6f3;
  --photo-b:#6f8fb0;
  --photo-c:#1e2a3c;
}
*{margin:0;padding:0;box-sizing:border-box}
html,body{width:1200px;height:798px;overflow:hidden;background:var(--page)}
.banner{
  position:absolute;left:0;top:170px;width:1200px;height:457px;overflow:hidden;
  background:radial-gradient(ellipse at 55% 45%,var(--ice-light) 0%,var(--ice-mid) 60%,var(--ice-deep) 100%);
  font-family:"Libre Caslon Text",serif;
}
.portrait{
  position:absolute;left:0;top:0;width:330px;height:457px;
  background:radial-gradient(ellipse at 62% 40%,var(--photo-a) 0%,var(--photo-b) 45%,var(--photo-c) 100%);
  -webkit-mask-image:linear-gradient(90deg,#000 75%,transparent 100%);
          mask-image:linear-gradient(90deg,#000 75%,transparent 100%);
}
.feature{position:absolute;left:330px;width:450px;top:0;height:457px;text-align:center;color:var(--navy)}
.artist{position:absolute;left:0;right:0;top:26px;font-family:"Pinyon Script",cursive;font-size:46px;line-height:1}
.album{position:absolute;left:0;right:0;top:85px;font-size:19px;letter-spacing:.5px}
.review{position:absolute;left:0;right:0}
.stars{font-size:30px;letter-spacing:2px;line-height:1;margin-bottom:2px}
.quote{font-size:14px;font-style:italic;font-weight:700;line-height:1.1;text-shadow:0 0 4px var(--white)}
.source{font-size:14px;line-height:1.1;text-shadow:0 0 4px var(--white)}
.dates{position:absolute;left:779px;top:0;width:421px;height:457px;background:linear-gradient(180deg,var(--panel) 0%,var(--panel-light) 100%)}
.dates-title{
  position:absolute;left:21px;top:13px;width:400px;height:47px;background:var(--header);
  color:var(--navy);font-weight:700;font-size:17px;line-height:47px;padding-left:50px;
}
.gig{position:absolute;left:0;width:410px;display:flex;color:var(--white);font-size:13.5px;line-height:1.05;text-transform:uppercase}
.gig .place{width:340px;text-align:right;padding-right:5px}
.gig .day{color:var(--navy);font-weight:700}
.tickets{position:absolute;right:34px;top:426px;color:var(--white);font-size:13.5px;line-height:1.2;text-align:right;text-transform:uppercase}
.tickets .url{display:block}
</style>
</head>
<body>
<section class="banner">
  <div class="portrait" role="img" aria-label="Portrait of the artist in a jewelled wire crown with icy blue makeup and long dark hair"></div>

  <div class="feature">
    <h1 class="artist">Clara Joy Halden</h1>
    <p class="album">LANTERN WALTZ</p>

    <div class="review" style="top:130px">
      <div class="stars">★★★★</div>
      <p class="quote">"VIBRANT AND EXPERIMENTAL"</p>
      <p class="source">-TUNEPATHS</p>
    </div>
    <div class="review" style="top:222px">
      <div class="stars">★★★★</div>
      <p class="quote">"OUTSTANDING, RICH AND EXPRESSIVE"</p>
      <p class="source">-BDM</p>
    </div>
    <div class="review" style="top:318px">
      <p class="quote">"IMPRESSIVE AND INVIGORATING"</p>
      <p class="source">-TBARKS</p>
    </div>
    <div class="review" style="top:384px">
      <p class="quote">"ENCHANTING"</p>
      <p class="source">-ACOUSTIC WIRE UK</p>
    </div>
  </div>

  <div class="dates">
    <h2 class="dates-title">AUTUMN/WINTER TOUR DATES</h2>
    <div class="gig" style="top:71px"><span class="place">Ravensby Folk Festival</span><span class="day">03/09</span></div>
    <div class="gig" style="top:97px"><span class="place">Swindon- Calder Theatre</span><span class="day">21/09</span></div>
    <div class="gig" style="top:123px"><span class="place">Hitchin- Brackwell Folk Club</span><span class="day">01/10</span></div>
    <div class="gig" style="top:149px"><span class="place">Bath- The Anvil</span><span class="day">17/10</span></div>
    <div class="gig" style="top:175px"><span class="place">Sheffield- Upper Dale Croquet Club</span><span class="day">20/10</span></div>
    <div class="gig" style="top:201px"><span class="place">Birmingham- Orchard Lamp Cafe</span><span class="day">24/10</span></div>
    <div class="gig" style="top:227px"><span class="place">Glasgow- The Nook and Jar</span><span class="day">26/10</span></div>
    <div class="gig" style="top:253px"><span class="place">Edinburgh - The Marble Parlour</span><span class="day">27/10</span></div>
    <div class="gig" style="top:279px"><span class="place">Capital Reel and Ballad Festival-<br>The Crooked Heron</span><span class="day">08/11</span></div>
    <div class="gig" style="top:319px"><span class="place">Lewes- Tandem Record Shop-<br>Live in Store</span><span class="day">25/11</span></div>
    <div class="gig" style="top:359px"><span class="place">Cambridge- The Quayside</span><span class="day">02/12</span></div>
    <div class="gig" style="top:385px"><span class="place">Lincolnshire- Fenmarsh Theatre</span><span class="day">27/01</span></div>
    <p class="tickets" style="top:410px">Tickets/Info:<span class="url">www.clarajoyhalden-music.example/gigs</span></p>
  </div>
</section>
</body>
</html>
```